Home Page and One Inside Page Needed for Engine Modify Site

Website that sells kits to modify and enhance your car engine performance. I don't like direction / design of current site at http://www.vortalmotorhaus.com.php61-24.sto3-2.pagedraftzone.com/

I want something modern. Something that shows power and performance.

I need home page and one inside page.

Keep blues and blacks and unfortunately that is their logo we have to work with. But this site needs WOW factor.

YOU DO NOT HAVE PERMISSION TO WORK OR SPEAK TO CLIENT DIRECTLY AND MUST WORK THROUGH ME.

```html
<!DOCTYPE html>
<html lang="en">
<head>
<meta charset="utf-8">
<title>Vortal Motorhaus — Pure Power</title>
<link rel="stylesheet" href="https://fonts.googleapis.com/css2?family=Raleway:wght@200;300;400;700;800&family=Open+Sans:wght@400&display=swap">
<style>
  :root {
    --navy: #0e3b74;
    --navy-deep: #0b3266;
    --accent: #5596f7;
    --white: #ffffff;
    --hero-bg: #160404;
    --hero-shade: #060505;
    --fire-core: #ffe9a8;
    --fire-mid: #f2a43a;
    --fire-edge: #7a2a08;
    --rule: #d8d8d8;
    --card-rule: #8a8a8a;
    --body-text: #444444;
  }
  * { margin: 0; padding: 0; box-sizing: border-box; }
  html, body { width: 1200px; height: 900px; overflow: hidden; }
  body {
    position: relative;
    background: var(--navy);
    font-family: "Raleway", sans-serif;
  }

  /* Header */
  .site-header {
    position: absolute; left: 0; top: 0; width: 1200px; height: 123px;
    background: linear-gradient(180deg, var(--navy) 0%, var(--navy-deep) 100%);
    border-bottom: 2px solid var(--rule);
  }
  .brand-name {
    position: absolute; left: 155px; top: 40px;
    font-size: 33px; font-weight: 400; letter-spacing: 0.5px;
    color: var(--white); text-transform: uppercase;
  }
  .main-nav {
    position: absolute; right: 157px; top: 52px;
    display: flex; gap: 12px;
  }
  .main-nav a {
    position: relative;
    font-size: 12.5px; font-weight: 700; color: var(--white);
    text-decoration: none; text-transform: uppercase;
  }
  .main-nav a.is-active::after {
    content: ""; position: absolute; left: 0; right: 0; top: 19px;
    height: 3px; background: var(--accent);
  }

  /* Hero */
  .hero {
    position: absolute; left: 0; top: 125px; width: 1200px; height: 570px;
    background: var(--hero-bg); overflow: hidden;
    border-bottom: 3px solid var(--rule);
  }
  .hero-shade { position: absolute; left: 0; top: 0; }
  .hero-visual {
    position: absolute; left: 100px; top: 85px; width: 500px; height: 410px;
    border-radius: 45%;
    background: radial-gradient(ellipse at 52% 50%, var(--fire-mid) 0%, var(--fire-core) 25%, var(--fire-mid) 50%, var(--fire-edge) 68%, rgba(22,4,4,0) 78%);
  }
  .hero-copy {
    position: absolute; right: 156px; top: 58px; text-align: right;
  }
  .hero-title {
    font-size: 124px; font-weight: 800; line-height: 104px;
    color: var(--accent); text-transform: uppercase; letter-spacing: 2px;
  }
  .hero-subtitle {
    margin-top: 18px;
    font-size: 41px; font-weight: 200; line-height: 40px;
    color: var(--white); text-transform: uppercase;
  }
  .hero-button {
    position: absolute; left: 794px; top: 439px; width: 250px; height: 55px;
    border-radius: 10px; background: var(--accent);
    color: var(--white); font-size: 24px; font-weight: 800;
    text-transform: uppercase; text-decoration: none;
    display: flex; align-items: center; justify-content: center;
  }

  /* Feature cards */
  .feature-card {
    position: absolute; top: 746px; width: 286px; height: 200px;
    background: var(--white); border-radius: 6px;
    padding: 20px 26px 0;
  }
  .feature-card:nth-child(1) { left: 145px; }
  .feature-card:nth-child(2) { left: 456px; }
  .feature-card:nth-child(3) { left: 769px; }
  .card-head {
    display: flex; align-items: center; gap: 16px;
    height: 50px; padding-bottom: 14px;
    border-bottom: 2px solid var(--card-rule);
    box-sizing: content-box;
  }
  .card-title {
    font-size: 18px; font-weight: 700; color: var(--accent);
    text-transform: uppercase;
  }
  .card-text {
    margin-top: 18px;
    font-family: "Open Sans", sans-serif; font-size: 13.5px; line-height: 23px;
    color: var(--body-text);
  }
</style>
</head>
<body>
  <header class="site-header">
    <div class="brand-name">Vortal Motorhaus</div>
    <nav class="main-nav">
      <a class="is-active" href="#">Home</a>
      <a href="#">Contact Us</a>
      <a href="#">How It Works</a>
      <a href="#">Product</a>
      <a href="#">Resources</a>
      <a href="#">About</a>
    </nav>
  </header>

  <section class="hero">
    <svg class="hero-shade" width="1200" height="570" viewBox="0 0 1200 570" aria-hidden="true">
      <polygon points="0,0 650,0 800,110 700,570 0,570" fill="var(--hero-shade)"/>
    </svg>
    <div class="hero-visual" role="img" aria-label="Chrome V8 engine bursting out of a fiery explosion"></div>
    <div class="hero-copy">
      <h1 class="hero-title">Pure<br>Power</h1>
      <p class="hero-subtitle">With our precision<br>exhaust header<br>modeling system</p>
    </div>
    <a class="hero-button" href="#">Find out more</a>
  </section>

  <main class="features">
    <article class="feature-card">
      <div class="card-head">
        <svg width="50" height="46" viewBox="0 0 50 46" aria-hidden="true">
          <path d="M2 4 L24 8 L24 44 L2 40 Z M48 4 L26 8 L26 44 L48 40 Z" fill="var(--accent)"/>
          <g stroke="var(--white)" stroke-width="2">
            <line x1="7" y1="14" x2="19" y2="16"/><line x1="7" y1="20" x2="19" y2="22"/>
            <line x1="7" y1="26" x2="19" y2="28"/><line x1="7" y1="32" x2="19" y2="34"/>
            <line x1="31" y1="16" x2="43" y2="14"/><line x1="31" y1="22" x2="43" y2="20"/>
            <line x1="31" y1="28" x2="43" y2="26"/><line x1="31" y1="34" x2="43" y2="32"/>
          </g>
        </svg>
        <h2 class="card-title">System Features</h2>
      </div>
      <p class="card-text">Lorem ipsum dolor sit amet, consectetur adipiscing elit. Donec</p>
    </article>
    <article class="feature-card">
      <div class="card-head">
        <svg width="48" height="48" viewBox="0 0 48 48" aria-hidden="true">
          <circle cx="24" cy="24" r="21" fill="none" stroke="var(--accent)" stroke-width="4"/>
          <path d="M17 19 a7 7 0 1 1 10 6 c-2 1 -3 2 -3 5 v1" fill="none" stroke="var(--accent)" stroke-width="4.5" stroke-linecap="round"/>
          <circle cx="24" cy="37" r="3" fill="var(--accent)"/>
        </svg>
        <h2 class="card-title">How It Works</h2>
      </div>
      <p class="card-text">Lorem ipsum dolor sit amet, consectetur adipiscing elit. Donec</p>
    </article>
    <article class="feature-card">
      <div class="card-head">
        <svg width="50" height="44" viewBox="0 0 50 44" aria-hidden="true">
          <path d="M2 22 Q25 -4 48 22 Q25 48 2 22 Z" fill="var(--accent)"/>
          <circle cx="25" cy="22" r="12" fill="var(--white)"/>
          <circle cx="25" cy="22" r="8" fill="var(--accent)"/>
        </svg>
        <h2 class="card-title">Our Gallery</h2>
      </div>
      <p class="card-text">Lorem ipsum dolor sit amet, consectetur adipiscing elit. Donec</p>
    </article>
  </main>
</body>
</html>
```